A Web3 (Blockchain) Company need a Web Design

Hi from NineRidgeLabs.
We need a web design for a Blockchain company focused on infrastructure. We are building infrastructure that make people with non-blockchain knowledge and experience can build blockchain platform/service easier.

Our logo will have bridge/road ambience.
We also think about some blue color.
But please propose your idea.

We want the website to represent us in "Reliable", "Secure", and "Make your blockchain related development easier".

I include sales deck to make you understand more about our business.
We expect the design to be in figma.

```html
<!DOCTYPE html>
<html lang="en">
<head>
<meta charset="utf-8">
<title>NineRidgeLabs — Web 3.0 Infrastructure</title>
<link href="https://fonts.googleapis.com/css2?family=Montserrat:ital,wght@0,400;0,500;0,600;0,700;0,800;1,800&display=swap" rel="stylesheet">
<style>
:root{
  --navy:#0c0b2a;
  --navy-2:#1b1a3d;
  --navy-3:#22214a;
  --teal:#2fe3c0;
  --teal-2:#22c7b1;
  --blue:#2a9be3;
  --ice:#eef6fc;
  --muted:#7f8ca8;
  --tab:#8a93b8;
  --white:#ffffff;
}
*{box-sizing:border-box;margin:0;padding:0}
html,body{width:1200px;height:4167px;overflow:hidden;background:#fff;font-family:"Montserrat",sans-serif}
.page{position:absolute;left:146px;top:8px;width:910px}
section,footer{position:relative;overflow:hidden}
.abs{position:absolute}

/* hero */
.hero{height:920px;background:var(--navy);color:var(--white)}
.hero-rise{position:absolute;left:0;top:356px;width:910px;height:250px}
.brand{display:flex;align-items:center;gap:8px;font-weight:600;letter-spacing:.08em}
.brand-mark{width:18px;height:18px;background:var(--teal);border-radius:3px}
.hero .brand{left:65px;top:42px;font-size:11px}
.nav{left:336px;top:44px;display:flex;gap:0;font-size:13px;font-weight:600}
.nav a{color:var(--white);text-decoration:none;position:absolute;white-space:nowrap}
.nav a.active{color:var(--teal)}
.contact-btn{left:760px;top:38px;width:90px;height:28px;border:1.5px solid var(--teal);border-radius:5px;font-size:12px;font-weight:600;display:flex;align-items:center;justify-content:center}
.hero-title{left:0;width:910px;top:180px;text-align:center;font-size:45px;font-weight:500;line-height:56px}
.hero-title .accent{color:var(--teal)}
.swoosh{left:185px;top:230px}
.hero-sub{left:0;width:910px;top:302px;text-align:center;font-size:15px;font-weight:500}
.hero-art{left:89px;top:356px;width:744px;height:251px;border-radius:8px;background:radial-gradient(ellipse at center,#2b2a5a 0%,#1b1a3d 55%,rgba(27,26,61,0) 80%)}
.trusted-label{left:65px;top:688px;font-size:13px;font-weight:500}
.trust-name{position:absolute;transform:translate(-50%,-50%);font-size:19px;font-weight:600;color:#8b8aab;white-space:nowrap}

/* trust system */
.trust{height:676px;background:var(--ice)}
.eyebrow{left:0;width:910px;text-align:center;font-size:20px;font-weight:500;color:var(--muted)}
.heading{left:0;width:910px;text-align:center;font-size:36px;font-weight:700;color:var(--navy)}
.diamond{position:absolute;width:171px;height:171px;border-radius:28px;background:var(--white);transform:rotate(45deg);box-shadow:0 10px 30px rgba(120,160,200,.25)}
.diamond.hot{background:linear-gradient(90deg,var(--blue),var(--teal))}
.diamond-body{position:absolute;width:150px;text-align:center;font-size:11px;font-weight:500;color:#2a2a40;line-height:14px}
.diamond-body.light{color:var(--white)}
.feature-icon{width:62px;height:62px;margin:0 auto 16px;border-radius:12px;background:linear-gradient(135deg,#3d7be6,#2fe3c0)}
.diamond-body.light .feature-icon{background:rgba(255,255,255,.85)}
.stem{width:2px;height:28px;margin:18px auto 0;background:#5d6f8a}
.diamond-body.light .stem{background:var(--white)}

/* advantage */
.advantage{height:663px;background:var(--navy);color:var(--white)}
.advantage .eyebrow{color:#b7b6d0}
.advantage .heading{color:var(--white)}
.rival-card{left:444px;top:241px;width:424px;height:275px;border-radius:16px;background:var(--navy-2)}
.chain-card{left:49px;top:214px;width:514px;height:320px;border-radius:16px;background:linear-gradient(90deg,#29c3d6,#33efc2);clip-path:polygon(0 0,100% 0,76.3% 100%,0 100%)}
.card-title{font-size:17px;font-weight:700}
.chain-title{left:92px;top:266px;color:var(--navy)}
.chain-line{right:506px;text-align:right;font-size:14px;font-weight:500;color:var(--navy);line-height:19px}
.rival-title{left:550px;top:279px;color:var(--teal)}
.rival-line{left:555px;font-size:14px;font-weight:500;line-height:19px}
.vs{left:447px;top:343px;width:82px;height:82px;border-radius:50%;background:var(--navy);border:5px solid var(--white);display:flex;align-items:center;justify-content:center;font-size:28px;font-weight:800;font-style:italic}

/* projects + team */
.projects{height:1598px;background:var(--ice)}
.tab{position:absolute;transform:translateX(-50%);text-align:center;font-size:17px;font-weight:600;line-height:22px;color:var(--tab);white-space:nowrap}
.tab.active{color:var(--teal-2)}
.tab-rail{left:29px;top:239px;width:849px;height:3px;background:#a3a9c8}
.tab-active{left:351px;top:238px;width:155px;height:4px;background:var(--teal-2)}
.tagline{left:0;width:910px;top:286px;text-align:center;font-size:14px;font-weight:500;color:var(--tab)}
.device-art{left:89px;top:324px;width:784px;height:465px;border-radius:18px;background:linear-gradient(180deg,#2a2f6b 0%,#4b3a9a 45%,#5c5e8a 85%,#c9ccd6 100%)}
.callout{position:absolute;display:flex;align-items:center;gap:14px;background:var(--white);border-radius:6px;padding:0 18px;box-shadow:0 8px 24px rgba(40,50,90,.18);font-size:11px;font-weight:600;color:var(--navy);line-height:14px}
.callout .dot{width:20px;height:20px;border-radius:50%;background:var(--teal);flex:none}
.callout .big{font-size:22px;font-weight:500;color:var(--teal-2);flex:none}
.callout .hl{color:var(--teal-2)}
.team-card{position:absolute;background:linear-gradient(180deg,#f4f4f4 0%,#dcdcdc 58%,#3ccab6 82%,#22bfae 100%);color:var(--white);overflow:hidden}
.portrait{position:absolute;left:0;top:0;width:100%;height:62%;background:linear-gradient(180deg,rgba(255,255,255,0) 0%,rgba(160,160,160,.35) 100%)}
.member{position:absolute;left:20px;right:16px;bottom:0}
.socials{display:flex;gap:8px;margin-bottom:12px}
.socials span{width:10px;height:10px;border-radius:50%;background:var(--white)}
.member-name{font-size:14px;font-weight:700;letter-spacing:.02em}
.member-role{font-size:12px;font-weight:500;margin-top:8px}
.member-note{font-size:9px;font-weight:600;margin-top:8px;line-height:12px}
.edge{position:absolute;top:1145px;width:16px;height:340px;background:linear-gradient(180deg,var(--ice) 55%,#2ec4b6 80%)}

/* footer */
.site-footer{height:294px;background:var(--navy);color:var(--white)}
.site-footer .brand{left:0;width:910px;top:58px;justify-content:center;font-size:16px;font-weight:500;letter-spacing:.14em}
.site-footer .brand-mark{width:30px;height:30px;border-radius:5px}
.rule{left:32px;top:133px;width:846px;height:1px;background:#4a4a6a}
.contact{position:absolute;top:166px;display:flex;align-items:center;gap:10px}
.contact-icon{width:28px;height:28px;border-radius:50%;background:var(--teal-2);display:flex;align-items:center;justify-content:center}
.contact-label{font-size:9px;font-weight:500;color:var(--teal)}
.contact-value{font-size:10px;font-weight:600;margin-top:3px}
.legal{top:250px;font-size:9px;font-weight:500;color:#b7b6d0}
</style>
</head>
<body>
<div class="page">

  <section class="hero">
    <svg class="hero-rise" viewBox="0 0 910 250" aria-hidden="true">
      <polygon points="0,215 455,0 910,215 910,250 0,250" fill="#1b1a3d"/>
    </svg>
    <div class="abs brand"><span class="brand-mark"></span>NINERIDGELABS</div>
    <nav class="abs nav">
      <a class="active" style="left:0">Services</a>
      <a style="left:76px">Features</a>
      <a style="left:155px">Projects</a>
      <a style="left:230px">Team</a>
    </nav>
    <div class="abs contact-btn">Contact Us</div>
    <h1 class="abs hero-title">NineRidgeLabs helps you<br>to tap into <span class="accent">WEB 3.0</span></h1>
    <svg class="abs swoosh" width="330" height="20" viewBox="0 0 330 20" aria-hidden="true">
      <path d="M4 14 C90 2 230 2 326 12" stroke="#2fe3c0" stroke-width="2.5" fill="none" stroke-linecap="round"/>
    </svg>
    <p class="abs hero-sub">Bridging you to the three point zero</p>
    <div class="abs hero-art" role="img" aria-label="Isometric illustration of a central Web 3.0 block linked to decentralisation, encryption and tokenisation nodes"></div>
    <p class="abs trusted-label">Trusted By</p>
    <span class="trust-name" style="left:123px;top:760px">HOURLY</span>
    <span class="trust-name" style="left:260px;top:760px">Stridewell</span>
    <span class="trust-name" style="left:401px;top:760px">Velaro</span>
    <span class="trust-name" style="left:538px;top:760px">R&amp;V</span>
    <span class="trust-name" style="left:679px;top:760px">MARENZI</span>
    <span class="trust-name" style="left:817px;top:760px">SWIFTO</span>
    <span class="trust-name" style="left:123px;top:841px">CORALINE</span>
    <span class="trust-name" style="left:260px;top:841px">Torvane</span>
    <span class="trust-name" style="left:401px;top:841px">kidoscope</span>
    <span class="trust-name" style="left:538px;top:841px">Halden</span>
    <span class="trust-name" style="left:679px;top:841px">LUMERA</span>
    <span class="trust-name" style="left:817px;top:841px">Kessel</span>
  </section>

  <section class="trust">
    <p class="abs eyebrow" style="top:66px">Blockchain as a</p>
    <h2 class="abs heading" style="top:100px">TRUST SYSTEM</h2>

    <div class="diamond" style="left:77px;top:235px"></div>
    <div class="diamond-body" style="left:87px;top:252px"><div class="feature-icon" role="img" aria-label="Replication network icon"></div>Replicated all around<br>the world<div class="stem"></div></div>

    <div class="diamond" style="left:373px;top:235px"></div>
    <div class="diamond-body" style="left:383px;top:252px"><div class="feature-icon" role="img" aria-label="Encrypted data icon"></div>Encrypted, secure<br>and immutable<div class="stem"></div></div>

    <div class="diamond" style="left:659px;top:235px"></div>
    <div class="diamond-body" style="left:669px;top:252px"><div class="feature-icon" role="img" aria-label="Insert-only database icon"></div>Can only use<br>Insert method<div class="stem"></div></div>

    <div class="diamond" style="left:228px;top:377px"></div>
    <div class="diamond-body" style="left:238px;top:394px"><div class="feature-icon" role="img" aria-label="Fingerprint identity icon"></div>Every insertion tied<br>to specific identity<div class="stem"></div></div>

    <div class="diamond hot" style="left:518px;top:377px"></div>
    <div class="diamond-body light" style="left:528px;top:394px"><div class="feature-icon" role="img" aria-label="Multi-party validation icon"></div>Every insertion are<br>validated by<br>multiple parties<div class="stem"></div></div>
  </section>

  <section class="advantage">
    <p class="abs eyebrow" style="top:59px">The advantage of</p>
    <h2 class="abs heading" style="top:91px">BLOCKCHAIN BASED DATABASE</h2>
    <div class="abs rival-card"></div>
    <div class="abs chain-card"></div>
    <h3 class="abs card-title chain-title">BLOCKCHAIN BASED DATABASE</h3>
    <p class="abs chain-line" style="top:308px">USD $500 for approximately 2 Million<br>transaction per month</p>
    <p class="abs chain-line" style="top:368px">Encrypted and Immutable</p>
    <p class="abs chain-line" style="top:405px">27k+ nodes across the world</p>
    <p class="abs chain-line" style="top:442px">Constant Latency</p>
    <h3 class="abs card-title rival-title">NON-BLOCKCHAIN DATABASE</h3>
    <p class="abs rival-line" style="top:322px">USD $39 for approximately 2 Million<br>transaction (25% insertion) per month</p>
    <p class="abs rival-line" style="top:384px">Not Encrypted</p>
    <p class="abs rival-line" style="top:421px">Single DRC</p>
    <p class="abs rival-line" style="top:457px">Increased Latency</p>
    <div class="abs vs">Vs</div>
  </section>

  <section class="projects">
    <p class="abs eyebrow" style="top:48px">NINERIDGELABS</p>
    <h2 class="abs heading" style="top:80px">PROJECTS</h2>
    <div class="tab" style="left:108px;top:169px">WHITE LABEL<br>WEB3 WALLET</div>
    <div class="tab" style="left:285px;top:169px">NFT<br>STARTER</div>
    <div class="tab active" style="left:427px;top:169px">RPC<br>NODES</div>
    <div class="tab" style="left:590px;top:169px">BLOCKCHAIN<br>API</div>
    <div class="tab" style="left:796px;top:169px">SOULBOUND<br>TOKEN STARTER</div>
    <div class="abs tab-rail"></div>
    <div class="abs tab-active"></div>
    <p class="abs tagline">makes your transaction faster and more reliable</p>
    <div class="abs device-art" role="img" aria-label="Laptop showing an isometric server farm of RPC nodes"></div>
    <div class="callout" style="left:73px;top:374px;width:283px;height:55px"><span class="dot"></span><span>Automatically included in any of<br><span class="hl">NineRidgeLabs</span> product</span></div>
    <div class="callout" style="left:558px;top:471px;width:282px;height:55px"><span class="big">1st</span><span>First Indonesian RPC Nodes, most<br>RPC Nodes are US/EU based.</span></div>
    <div class="callout" style="left:44px;top:529px;width:283px;height:55px"><span class="dot"></span><span>In partnership with one of the<br>biggest server provider in Indonesia</span></div>
    <div class="callout" style="left:501px;top:606px;width:283px;height:54px"><span class="big">15x</span><span>15x faster than default RPC Nodes</span></div>

    <p class="abs eyebrow" style="top:931px">Our Team</p>
    <h2 class="abs heading" style="top:963px">OUR EXPERTS</h2>

    <div class="edge" style="left:0"></div>
    <div class="edge" style="left:894px"></div>

    <div class="team-card" style="left:24px;top:1145px;width:280px;height:340px">
      <div class="portrait" role="img" aria-label="Black and white portrait of the chief executive officer"></div>
      <div class="member" style="bottom:16px">
        <div class="socials"><span></span><span></span><span></span></div>
        <div class="member-name">RAKA PRADIPTA</div>
        <div class="member-role">Cheif Executive Officer</div>
        <div class="member-note">Builds infrastructure for digital billing in<br>Indonesia since 2005.</div>
      </div>
    </div>

    <div class="team-card" style="left:315px;top:1113px;width:278px;height:402px">
      <div class="portrait" role="img" aria-label="Black and white portrait of the chief technical officer"></div>
      <div class="member" style="bottom:30px">
        <div class="socials"><span></span><span></span><span></span></div>
        <div class="member-name">DIMAS SANTOSO</div>
        <div class="member-role">Cheif Technical Officer</div>
        <div class="member-note">Verdant 30 Under 30 Indonesia Tech Rockstar</div>
      </div>
    </div>

    <div class="team-card" style="left:605px;top:1145px;width:280px;height:340px">
      <div class="portrait" role="img" aria-label="Black and white portrait of a founding team member"></div>
      <div class="member" style="bottom:16px">
        <div class="socials"><span></span><span></span><span></span></div>
        <div class="member-name">KEVIN LESMANA</div>
        <div class="member-role">Founding Team</div>
        <div class="member-note">Web3 Games and Launchpads Serial<br>Entrepreneur</div>
      </div>
    </div>
  </section>

  <footer class="site-footer">
    <div class="abs brand"><span class="brand-mark"></span>NINERIDGELABS</div>
    <div class="abs rule"></div>
    <div class="contact" style="left:74px">
      <span class="contact-icon"><svg width="14" height="14" viewBox="0 0 24 24" aria-hidden="true"><path d="M12 2a7 7 0 0 0-7 7c0 5 7 13 7 13s7-8 7-13a7 7 0 0 0-7-7zm0 9.5A2.5 2.5 0 1 1 12 6.5a2.5 2.5 0 0 1 0 5z" fill="#fff"/></svg></span>
      <div><div class="contact-label">Address</div><div class="contact-value">Jl. Cendana 12, Bandarsari</div></div>
    </div>
    <div class="contact" style="left:415px">
      <span class="contact-icon"><svg width="14" height="14" viewBox="0 0 24 24" aria-hidden="true"><path d="M6.6 10.8a15 15 0 0 0 6.6 6.6l2.2-2.2a1 1 0 0 1 1-.25 11.4 11.4 0 0 0 3.6.57 1 1 0 0 1 1 1V20a1 1 0 0 1-1 1A17 17 0 0 1 3 4a1 1 0 0 1 1-1h3.5a1 1 0 0 1 1 1c0 1.25.2 2.45.57 3.6a1 1 0 0 1-.25 1z" fill="#fff"/></svg></span>
      <div><div class="contact-label">Phone</div><div class="contact-value">XXXXX-XXXXXX_XXXX</div></div>
    </div>
    <div class="contact" style="left:704px">
      <span class="contact-icon"><svg width="14" height="14" viewBox="0 0 24 24" aria-hidden="true"><path d="M2 12 22 3l-9 19-2-8z" fill="#fff"/></svg></span>
      <div><div class="contact-label">E-mail</div><div class="contact-value">hello@nineridgelabs.example</div></div>
    </div>
    <p class="abs legal" style="left:84px">© 2022 NINERIDGELABS LLC. ALL RIGHTS RESERVED.</p>
    <p class="abs legal" style="left:754px">PRIVACY POLICY</p>
  </footer>

</div>
</body>
</html>
```